TBL Enterprises has 5 divisions in the organisation.
One of them is our Soaps, Candles and Cosmetics range.

Our Logo is a MERIN with the word MERIN an image of a crown.
Merin Supplements & Merin Sports are 2 divisions.

Now we need to introduce our MERIN COLLECTIONS which will include cosmetic, candles, fragrances etc.

What we need designed is an elegant, sophisticated label of our CANDLE JARS and Outer Box.

The same will flow through to our soaps and other collection.

This will the beginning of a long term relationship for the designer to maintain and update our Merin Collections artwork.

Hello designers,

We have increases our 1st prize budget to $200.00

Please read the brief carefully.
We need this job wrapped up quickly.

It is a fairly simple project with huge long term potential.

We look forward to receiving some designs.

Reason: Due to the Easter Break last week, many people were off work. Therefore we have extended our deadline to allow other participants to submit their designs.

Reason: We have not found a design we like yet.

Industry/Entity Type

Cosmetics

Requirements
Must have
• The MERIN and the word MERIN must remain the same.
The word collections must be added under the crown.
The word collections to be Elegant, maybe cursive, or hand written.

Wording for Jar Label:
100% Soy Wax
Quality Essential oils & Fragrances
Hand made in Australia

Box Wording:
will be provided at later stage.
Make a mockup of a box but not too loud.
Sophisticated and elegant.
Do not use existing artwork from others.

Nice to have
• Special design label.

The width of the label to be no more than 50mm.
The height of the label to be no more than 60mm

We believe that the JAR label needs to be small and effective.
We beleive the box should use Royal colours and not too many flowers and vines. Elegance.
Should not have
• Should not be noisy, loud and full of information.

```html
<!DOCTYPE html>
<html lang="en">
<head>
<meta charset="utf-8">
<title>Merin Collections – Candle Jar Label</title>
<link rel="stylesheet" href="https://fonts.googleapis.com/css2?family=Libre+Baskerville:wght@400&family=Pinyon+Script&family=Archivo+Narrow:wght@400&display=swap">
<style>
  :root {
    --canvas: #ffffff;
    --royal-purple: #341452;
    --gold: #c9a43e;
    --gold-light: #e3c766;
    --gold-dark: #8a6a1c;
    --flourish-tone: #4a2a66;
  }
  * { margin: 0; padding: 0; box-sizing: border-box; }
  html, body {
    width: 1200px;
    height: 777px;
    overflow: hidden;
    background: var(--canvas);
  }
  .canvas {
    position: relative;
    width: 1200px;
    height: 777px;
  }
  .jar-label {
    position: absolute;
    left: 370px;
    top: 102px;
    width: 460px;
    height: 572px;
    padding: 13px;
    background: linear-gradient(135deg, var(--gold-dark), var(--gold-light) 35%, var(--gold) 60%, var(--gold-dark));
  }
  .label-face {
    position: relative;
    width: 100%;
    height: 100%;
    background: var(--royal-purple);
    color: var(--gold);
    text-align: center;
  }
  .brand-name {
    position: absolute;
    left: 0; right: 0;
    top: 72px;
    font-family: "Libre Baskerville", serif;
    font-size: 34px;
    letter-spacing: 1px;
    color: var(--gold);
  }
  .collection-title {
    position: absolute;
    left: 0; right: 0;
    top: 150px;
    font-family: "Pinyon Script", cursive;
    font-size: 76px;
    line-height: 1;
    color: var(--gold);
  }
  .flourish {
    position: absolute;
    left: 142px;
    top: 272px;
    width: 150px;
    height: 44px;
  }
  .product-claims {
    position: absolute;
    left: 0; right: 0;
    top: 352px;
    font-family: "Archivo Narrow", sans-serif;
    font-size: 23px;
    line-height: 33px;
    color: var(--gold-light);
  }
  .origin-note {
    position: absolute;
    left: 0; right: 0;
    top: 502px;
    font-family: "Pinyon Script", cursive;
    font-size: 26px;
    color: var(--gold);
    opacity: 0.85;
  }
</style>
</head>
<body>
<div class="canvas">
  <section class="jar-label">
    <div class="label-face">
      <div class="brand-name">MERIN</div>
      <div class="collection-title">Collections</div>
      <svg class="flourish" viewBox="0 0 150 44" role="img" aria-label="Pair of gold scroll flourishes">
        <rect x="0" y="0" width="150" height="44" rx="6" fill="var(--flourish-tone)"/>
      </svg>
      <div class="product-claims">
        <p>100% Soy Wax</p>
        <p>Quality Essential oils &amp; Fragrances</p>
      </div>
      <div class="origin-note">Hand made in Australia</div>
    </div>
  </section>
</div>
</body>
</html>
```